Scholarly Pathways - educational consulting

I am beginning an educational consultation business - focusing on Tribal (Native American Indian) Communities, but will work with anyone. I have work experience in K-12 and Higher Education. Special Education - transition from school to work. Advising and facilitating with academic skills in higher education. I have a BS - Special Education, Masters - Educational Administration and working on a PhD in Higher Education. Also completing PMB approved certification as an Academic Life Coach

Target Market(s)

K12 college bound students and parents, Kinfolk Crossings college bound students and families, special education college bound students and parents

Industry/Entity Type

Business

Contact Information for Business Card

Marnie Odell Fenwick. PO Box 417, Fernridge, ST 00417. (918) 555-0293. marnie@scholarlypathways.example

Requirements
Must have
• Scholarly Pathways is the name of the business - Kinfolk Crossings is a focus area
Nice to have
• Tourquoise would be nice. I do not have a logo yet

```html
<!DOCTYPE html>
<html lang="en">
<head>
<meta charset="utf-8">
<title>Scholarly Pathways – Business Card</title>
<link rel="stylesheet" href="https://fonts.googleapis.com/css2?family=Open+Sans:wght@400;600;700&display=swap">
<style>
  :root {
    --page-bg: #e9e7e3;
    --card-dark: #0c0f12;
    --card-dark-edge: #1d2328;
    --card-light: #ffffff;
    --brand-blue: #1b8fc8;
    --ink: #111111;
    --ink-soft: #2a2a2a;
    --on-dark: #e8eef2;
    --ghost: #e3e6e9;
    --band: #0b0b0b;
  }
  * { box-sizing: border-box; margin: 0; padding: 0; }
  html, body {
    width: 1200px; height: 784px; overflow: hidden;
    background: var(--page-bg);
    font-family: "Open Sans", Arial, sans-serif;
  }
  .stage {
    width: 1200px; height: 784px;
    display: flex; align-items: center; justify-content: center; gap: 40px;
  }
  .card {
    position: relative;
    width: 540px; height: 309px;
    border-radius: 4px;
    overflow: hidden;
    box-shadow: 0 6px 18px rgba(0,0,0,.18);
  }

  /* Back of card */
  .card--back {
    background: radial-gradient(ellipse at 50% 30%, var(--card-dark-edge) 0%, var(--card-dark) 70%);
    color: var(--on-dark);
    text-align: center;
  }
  .back-brand {
    position: absolute; top: 58px; left: 0; right: 0;
    display: flex; align-items: center; justify-content: center; gap: 12px;
  }
  .brand-dot {
    width: 46px; height: 46px; border-radius: 50%;
    background: var(--brand-blue);
    flex: none;
  }
  .back-brand .brand-name {
    font-size: 24px; font-weight: 600; color: var(--brand-blue);
  }
  .focus {
    position: absolute; top: 148px; left: 0; right: 0;
    line-height: 1.4;
  }
  .focus-title { font-size: 13px; letter-spacing: .3px; margin-bottom: 8px; }
  .focus-item { font-size: 13px; }

  /* Front of card */
  .card--front { background: var(--card-light); color: var(--ink); }
  .front-brand {
    position: absolute; top: 44px; left: 34px;
    display: flex; align-items: center; gap: 14px;
  }
  .front-brand .brand-dot { width: 70px; height: 70px; }
  .front-brand .brand-name {
    font-size: 26px; font-weight: 700; color: var(--ink);
  }
  .ghost-mark {
    position: absolute; right: -30px; top: 96px;
    width: 150px; height: 150px; border-radius: 50%;
    background: var(--ghost);
  }
  .holder { position: absolute; left: 34px; top: 150px; }
  .holder-name { font-size: 21px; font-weight: 600; color: var(--brand-blue); line-height: 1.1; }
  .holder-role { font-size: 13px; color: var(--ink-soft); margin-top: 3px; }
  .contact { position: absolute; left: 34px; top: 204px; list-style: none; }
  .contact li {
    display: flex; align-items: center; gap: 7px;
    font-size: 14px; line-height: 21px; color: var(--ink);
  }
  .contact svg { width: 15px; height: 15px; fill: var(--brand-blue); flex: none; }
  .front-rule {
    position: absolute; left: 0; right: 0; bottom: 32px; height: 4px;
    background: var(--brand-blue);
  }
  .front-band {
    position: absolute; left: 0; right: 0; bottom: 0; height: 32px;
    background: var(--band);
  }
</style>
</head>
<body>
<main class="stage">

  <section class="card card--back" aria-label="Card back">
    <div class="back-brand">
      <span class="brand-dot"></span>
      <span class="brand-name">Scholarly Pathways</span>
    </div>
    <div class="focus">
      <p class="focus-title">AREAS OF FOCUS: KINFOLK CROSSINGS (NATIVE AMERICAN)</p>
      <p class="focus-item">K12-college, Academic Life Coach,</p>
      <p class="focus-item">K-12 - College Transitions and Special Education</p>
      <p class="focus-item">K-12 - College Transitions</p>
    </div>
  </section>

  <section class="card card--front" aria-label="Card front">
    <div class="ghost-mark"></div>
    <div class="front-brand">
      <span class="brand-dot"></span>
      <span class="brand-name">Scholarly Pathways</span>
    </div>
    <div class="holder">
      <p class="holder-name">Marnie Odell Fenwick</p>
      <p class="holder-role">Manager</p>
    </div>
    <ul class="contact">
      <li>
        <svg viewBox="0 0 24 24" aria-hidden="true"><path d="M6.6 10.8a15.1 15.1 0 0 0 6.6 6.6l2.2-2.2a1 1 0 0 1 1-.25 11.4 11.4 0 0 0 3.6.57 1 1 0 0 1 1 1V20a1 1 0 0 1-1 1A17 17 0 0 1 3 4a1 1 0 0 1 1-1h3.5a1 1 0 0 1 1 1c0 1.25.2 2.45.57 3.57a1 1 0 0 1-.25 1z"/></svg>
        000.555.0293
      </li>
      <li>
        <svg viewBox="0 0 24 24" aria-hidden="true"><path d="M2 5h20v14H2zm2 2v.4l8 5.3 8-5.3V7zm0 2.8V17h16V9.8l-8 5.3z"/></svg>
        marnie@scholarlypathways.example
      </li>
      <li>
        <svg viewBox="0 0 24 24" aria-hidden="true"><path d="M12 3 2 12h3v8h5v-6h4v6h5v-8h3z"/></svg>
        PO Box 417, Fernridge, ST 00417
      </li>
    </ul>
    <div class="front-rule"></div>
    <div class="front-band"></div>
  </section>

</main>
</body>
</html>
```